BRMSC redesign and update stationary bc envelopes.

Stationary, Envelopes, Brochures, Business Card. Need to add second surgeon and two other offices. I need everything to match. I am a oral & maxillofacial surgeon.
Additional surgeon and three office addresses.
Tae Woo Park, DMD, MD, INC

3178 Silver Meadow Boulevard
Cedar Ridge, CA 95410

612 Lorel Lane, Suite 210
Maple Grove, CA. 95521

2375 Birch Avenue, Suite 340
Pine Hollow, CA. 95688
Updates

Logo design uploaded. Zapfino Extra/Adobe Garamond/Palatino are fonts used before. Not sure what is on exisiting stationary.

Target Market(s)

Referral dentist and sometimes patients. I am a oral & Maxillofacial surgeon.

Industry/Entity Type

Dental Clinic

Font styles to use
Serif
Script

Requirements
Must have
• Color of existing stationary. Update is possible.
Nice to have
• Conservative/modern
Should not have
• Playful

```html
<!DOCTYPE html>
<html lang="en">
<head>
<meta charset="utf-8">
<title>BRMSC Business Card</title>
<link rel="stylesheet" href="https://fonts.googleapis.com/css2?family=Montserrat:wght@400;600;700&family=Questrial&display=swap">
<style>
  :root {
    --bg: #ece8e3;
    --card: #ffffff;
    --brown: #4a260f;
    --green: #7a9a3a;
    --text: #4f4f4f;
    --sky: #e2ecf3;
    --arc: #cfdc8e;
    --hill-green: #cfe0a6;
    --hill-gold: #f3e3a6;
  }
  * { margin: 0; padding: 0; box-sizing: border-box; }
  html, body { width: 1200px; height: 1200px; overflow: hidden; background: var(--bg); }
  body { position: relative; font-family: "Montserrat", sans-serif; }

  .card {
    position: absolute;
    left: 160px;
    width: 880px;
    height: 502px;
    background: var(--card);
    border-radius: 26px;
    overflow: hidden;
    box-shadow: 0 6px 18px rgba(0,0,0,0.18);
  }
  .card--front { top: 36px; }
  .card--back { top: 664px; }

  .front-curve { position: absolute; inset: 0; }

  .contact { position: absolute; left: 44px; top: 52px; color: var(--text); }
  .doctor { font-weight: 700; color: var(--brown); font-size: 26px; line-height: 30px; letter-spacing: 0.2px; }
  .doctor .cred { font-size: 15px; font-weight: 700; }
  .board { margin-top: 6px; color: var(--green); font-size: 17.5px; line-height: 25px; font-weight: 400; }
  .offices { margin-top: 30px; }
  .office { font-size: 17.5px; line-height: 24.5px; margin-bottom: 6px; }
  .reach { margin-top: 12px; font-size: 17.5px; line-height: 25px; }

  .brand {
    position: absolute;
    left: 580px;
    top: 392px;
    width: 220px;
    text-align: center;
    font-family: "Montserrat", sans-serif;
    font-weight: 600;
    font-size: 36px;
    letter-spacing: 3px;
    color: var(--brown);
  }

  .landscape {
    position: absolute;
    left: 0; top: 0;
    width: 880px; height: 390px;
    background:
      linear-gradient(180deg, var(--sky) 0%, #eef2e4 35%, var(--hill-green) 55%, var(--hill-gold) 78%, #ffffff 100%);
  }
  .services {
    position: absolute;
    left: 0; right: 0; top: 390px;
    text-align: center;
    font-family: "Questrial", sans-serif;
    font-size: 19.5px;
    line-height: 25px;
    color: var(--text);
  }
</style>
</head>
<body>

  <section class="card card--front">
    <svg class="front-curve" width="880" height="502" viewBox="0 0 880 502" aria-hidden="true">
      <path d="M462 0 Q760 90 872 470 L880 470 L880 0 Z" fill="var(--sky)"/>
      <path d="M470 4 Q772 108 862 462" fill="none" stroke="var(--arc)" stroke-width="5" stroke-linecap="round"/>
    </svg>

    <div class="contact">
      <p class="doctor">Martin J. Halloway, <span class="cred">DDS, Inc</span></p>
      <p class="doctor">Tae Woo Park, <span class="cred">DMD, MD, INC</span></p>
      <p class="board">Diplomate of the Pacific College of<br>Oral &amp; Facial Surgical Care</p>

      <div class="offices">
        <p class="office">3178 Silver Meadow Boulevard<br>Cedar Ridge, CA 95410</p>
        <p class="office">612 Lorel Lane, Suite 210<br>Maple Grove, CA. 95521</p>
        <p class="office">2375 Birch Avenue, Suite 340<br>Pine Hollow, CA. 95688</p>
      </div>

      <div class="reach">
        <p>916.555.0142 | 916.555.0187</p>
        <p>drhalloway@brmscoralsurgery.com</p>
        <p>www.brmscoralsurgery.com</p>
      </div>
    </div>

    <p class="brand">BRMSC</p>
  </section>

  <section class="card card--back">
    <div class="landscape" role="img" aria-label="Soft watercolour illustration of green foothills and golden rolling fields under a pale blue sky"></div>
    <div class="services">
      <p>Dentoalveolar Surgery | Dental Implant Surgery</p>
      <p>Orthognathic Surgery | Facial Trauma Surgery | Preprosthetic &amp; Reconstructive Surgery</p>
      <p>TMJ Disorders &amp; Surgery | Obstructive Sleep Apnea Surgery</p>
    </div>
  </section>

</body>
</html>
```